Tamkor, a service provider dedicated to improving the performance of a website

Tamkor offers optimization and performance improvement for all types of websites (showcase sites, e-commerce, ...), with the aim of improving their ranking on Vintrel and their customer transformation rate. The main benefits consist in optimizing the factors of a site. In addition, we also offer content creation (description of product sheets, services, ...), Vintrel Ads campaign management, migration version for Prestashop / Wordpress, etc. The design must be a fresh image, dynamic, why not "fun", but also serious. No favorite color, carte blanche on this point;)

```html
<!DOCTYPE html>
<html lang="en">
<head>
<meta charset="utf-8">
<title>Tamkor business cards</title>
<link href="https://fonts.googleapis.com/css2?family=Poppins:wght@400;500;600;700&display=swap" rel="stylesheet">
<style>
  :root {
    --bg: #2b2b2d;
    --card-blue: #3a55a4;
    --card-blue-deep: #2f4792;
    --ink-white: #ffffff;
    --ink-soft: #e8ecf8;
    --logo-front: #7fa8ff;
  }
  * { margin: 0; padding: 0; box-sizing: border-box; }
  html, body {
    width: 1200px;
    height: 960px;
    overflow: hidden;
    background: var(--bg);
    font-family: "Poppins", sans-serif;
  }
  .canvas {
    position: relative;
    width: 1200px;
    height: 960px;
  }
  .card {
    position: absolute;
    width: 560px;
    height: 320px;
    border-radius: 22px;
    background: var(--card-blue);
    overflow: hidden;
    box-shadow: 0 18px 40px rgba(0, 0, 0, 0.45);
  }
  .card-front { left: 60px; top: 140px; }
  .card-back { left: 580px; top: 500px; }

  .front-content {
    position: absolute;
    inset: 0;
    display: flex;
    flex-direction: column;
    align-items: center;
    justify-content: center;
    gap: 18px;
  }
  .brand-name {
    font-weight: 700;
    line-height: 1;
    letter-spacing: -0.02em;
  }
  .front-content .brand-name {
    font-size: 92px;
    color: var(--logo-front);
  }
  .website {
    font-size: 17px;
    font-weight: 500;
    letter-spacing: 0.28em;
    color: var(--ink-white);
  }

  .corner-tile {
    position: absolute;
    right: -40px;
    top: -40px;
    width: 250px;
    height: 220px;
    border-radius: 40px;
    background: var(--card-blue-deep);
  }
  .back-content {
    position: absolute;
    left: 48px;
    bottom: 34px;
    color: var(--ink-white);
  }
  .back-content .brand-name {
    font-size: 78px;
    color: var(--ink-white);
    margin-bottom: 16px;
  }
  .person-name {
    font-size: 19px;
    font-weight: 600;
    letter-spacing: 0.02em;
    text-transform: uppercase;
    line-height: 1.15;
  }
  .person-role {
    font-size: 16px;
    color: var(--ink-soft);
    margin-bottom: 12px;
  }
  .address, .contacts {
    font-size: 14px;
    line-height: 1.45;
    color: var(--ink-soft);
  }
  .address { margin-bottom: 10px; }
  .contacts {
    display: grid;
    grid-template-columns: auto auto;
    column-gap: 22px;
  }
</style>
</head>
<body>
<main class="canvas">
  <section class="card card-front" aria-label="Card front">
    <div class="front-content">
      <div class="brand-name">Tamkor</div>
      <div class="website">WWW.TAMKOR.COM</div>
    </div>
  </section>

  <section class="card card-back" aria-label="Card back">
    <div class="corner-tile"></div>
    <div class="back-content">
      <div class="brand-name">Tamkor</div>
      <div class="person-name">Daniel Reyes</div>
      <div class="person-role">President</div>
      <div class="address">2140 Larkspur Road<br>Fairbanks, Alaska 99701</div>
      <div class="contacts">
        <span>P : 555-204-7731</span><span>M : 555-618-2390</span>
        <span>F : 555-347-1186</span><span>E : info@tamkor.com</span>
      </div>
    </div>
  </section>
</main>
</body>
</html>
```